Mexican construction company needs a business card design

We need a business card design for a company based in Monterrey, Mexico called:

Desarrollos Tolvani S.A. de C.V.

The company is in the construction business and I would like the businees card to be simple and concise. Please use white background and blue or black text color that say:

"Proyectos de Construcción"-- (Brief description of business)
" Rodrigo Ulloa Benítez"--- (My name)
"rulloab@correovelo.mx"-- (My email)
"C: (81) 82 19 57 46"-- (My cell)
"O: (81) 86 72 13 95"-- (Office phone)

Please use only the colors of my company that are attached

Please make the back of the business card blue (same blue from logo) and use the logo.

Thanks!

```html
<!DOCTYPE html>
<html lang="es">
<head>
<meta charset="UTF-8">
<title>Desarrollos Tolvani — Tarjeta de presentación</title>
<link rel="stylesheet" href="https://fonts.googleapis.com/css2?family=Open+Sans:wght@400;600;700&display=swap">
<style>
  :root {
    --backdrop: #1c1c1e;
    --navy: #1e1a5a;
    --navy-light: #34307a;
    --white: #ffffff;
    --ink: #1e1a5a;
    --text-dark: #222233;
    --mark-grey: #9a9aa6;
  }
  * { margin: 0; padding: 0; box-sizing: border-box; }
  html, body {
    width: 1200px; height: 900px; overflow: hidden;
    background: var(--backdrop);
    font-family: "Open Sans", Arial, sans-serif;
  }
  .canvas { position: relative; width: 1200px; height: 900px; }

  .card {
    position: absolute; width: 640px; height: 366px;
    border-radius: 4px; overflow: hidden;
    box-shadow: 0 18px 40px rgba(0,0,0,.55);
  }

  /* Back of card */
  .card-back {
    left: 170px; top: 80px;
    background: linear-gradient(100deg, var(--navy) 0%, var(--navy) 45%, var(--navy-light) 100%);
  }
  .brand { position: absolute; display: flex; align-items: center; gap: 22px; }
  .card-back .brand { left: 90px; top: 118px; }
  .brand-square { border: 6px solid currentColor; flex: none; }
  .card-back .brand-square { width: 92px; height: 92px; color: var(--mark-grey); }
  .brand-name {
    font-weight: 600; text-transform: uppercase; letter-spacing: .12em; line-height: 1.05;
    white-space: nowrap;
  }
  .card-back .brand-name { color: var(--white); font-size: 34px; }
  .brand-name span { display: block; }
  .brand-name .small { font-size: .72em; }

  /* Front of card */
  .card-front { left: 390px; top: 440px; background: var(--white); }
  .card-front .wave { position: absolute; inset: 0; }
  .card-front .brand { left: 60px; top: 110px; gap: 14px; }
  .card-front .brand-square { width: 46px; height: 46px; border-width: 4px; color: var(--mark-grey); }
  .card-front .brand-name { color: var(--ink); font-size: 22px; }

  .person { position: absolute; left: 375px; top: 30px; white-space: nowrap; }
  .person-name { font-weight: 700; font-size: 21px; line-height: 1.3; color: var(--ink); }
  .person-role { font-size: 14px; line-height: 1.4; color: var(--text-dark); margin-left: 14px; letter-spacing: .03em; }

  .contact { position: absolute; left: 72px; top: 246px; list-style: none; }
  .contact li {
    display: flex; align-items: center; gap: 14px; white-space: nowrap;
    font-size: 15px; color: var(--text-dark); height: 28px; letter-spacing: .03em;
  }
  .contact svg { width: 14px; height: 14px; flex: none; fill: var(--ink); }
</style>
</head>
<body>
<main class="canvas">
  <section class="card card-back" aria-label="Reverso de la tarjeta">
    <div class="brand">
      <div class="brand-square"></div>
      <div class="brand-name"><span class="small">Desarrollos</span><span>Tolvani</span></div>
    </div>
  </section>

  <section class="card card-front" aria-label="Frente de la tarjeta">
    <svg class="wave" viewBox="0 0 640 366" preserveAspectRatio="none" aria-hidden="true">
      <defs>
        <linearGradient id="waveFill" x1="0" y1="0" x2="1" y2="0">
          <stop offset="0" stop-color="#1e1a5a"/>
          <stop offset="1" stop-color="#34307a"/>
        </linearGradient>
      </defs>
      <path d="M360 165 C440 112 530 96 640 98 L640 108 C540 108 450 124 360 165 Z" fill="#1e1a5a"/>
      <path d="M640 124 C545 120 475 158 432 218 C385 295 325 350 235 366 L640 366 Z" fill="url(#waveFill)"/>
      <path d="M205 362 C305 340 380 292 428 226" fill="none" stroke="#ffffff" stroke-width="3" opacity=".8"/>
    </svg>

    <div class="person">
      <p class="person-name">Rodrigo Ulloa Benítez</p>
      <p class="person-role">Manager</p>
    </div>

    <div class="brand">
      <div class="brand-square"></div>
      <div class="brand-name"><span class="small">Desarrollos</span><span>Tolvani</span></div>
    </div>

    <ul class="contact">
      <li>
        <svg viewBox="0 0 24 24" aria-hidden="true"><path d="M6.6 10.8a15 15 0 0 0 6.6 6.6l2.2-2.2c.3-.3.7-.4 1-.2 1.1.4 2.3.6 3.6.6.6 0 1 .4 1 1V20c0 .6-.4 1-1 1A17 17 0 0 1 3 4c0-.6.4-1 1-1h3.5c.6 0 1 .4 1 1 0 1.3.2 2.5.6 3.6.1.3 0 .7-.2 1z"/></svg>
        <span>(81) 86 72 13 95</span>
      </li>
      <li>
        <svg viewBox="0 0 24 24" aria-hidden="true"><path d="M7 2h10a2 2 0 0 1 2 2v16a2 2 0 0 1-2 2H7a2 2 0 0 1-2-2V4a2 2 0 0 1 2-2zm0 3v12h10V5zm5 13.5a1 1 0 1 0 0 2 1 1 0 0 0 0-2z"/></svg>
        <span>(81) 82 19 57 46</span>
      </li>
      <li>
        <svg viewBox="0 0 24 24" aria-hidden="true"><path d="M12 2a10 10 0 1 0 5 18.7l-.9-1.7A8 8 0 1 1 20 12v1.2c0 1-.7 1.8-1.5 1.8S17 14.2 17 13.2V7h-2v1a5 5 0 1 0 .6 7.3A3.4 3.4 0 0 0 18.5 17c2 0 3.5-1.7 3.5-3.8V12A10 10 0 0 0 12 2zm0 13a3 3 0 1 1 0-6 3 3 0 0 1 0 6z"/></svg>
        <span>rulloab@correovelo.mx</span>
      </li>
    </ul>
  </section>
</main>
</body>
</html>
```